Marketing company needs A5 flyer

My organisation needs a flyer designed to hand out at an upcoming loyalty conference that we are running.

The flyer is to be handed out to delegates to promote our services.

I have mocked up something - see attached. It includes the copy. Please feel free to use your creativity, don't feel as though you need to stick to this design at all - however the copy included needs to remain.

This is to be a 2 sided flyer. the information the back with include logos and testimonials of 3 of our clients (Talbrook, Vessock and Dorquin). The logos and testimonials can be found here http://brightpathrewards.com.au/clients/

Please make do with the logos on the web as well as the JPEG i have attached, if it's absolutely necessary that I source larger files i will try to do so.

I've also attached the powerpoint template we use, feel free to incorporate the 'blue swirl' if you see fit.

```html
<!DOCTYPE html>
<html lang="en">
<head>
<meta charset="utf-8">
<title>Brightpath Rewards – A5 Flyer</title>
<link rel="stylesheet" href="https://fonts.googleapis.com/css2?family=Arimo:wght@400;700&family=Oswald:wght@500;600&display=swap">
<style>
  :root {
    --bg: #4a4a4a;
    --paper: #ffffff;
    --navy: #1f3f8f;
    --blue: #2b63b8;
    --blue-light: #4a8fd6;
    --blue-pale: #8ec5ee;
    --ink: #3a3a3a;
    --grey: #5b5b5b;
    --bar: #34363b;
    --welcome: #d9dde6;
  }
  * { box-sizing: border-box; margin: 0; padding: 0; }
  html, body { width: 1200px; height: 900px; overflow: hidden; }
  body {
    background: var(--bg);
    font-family: "Arimo", Arial, sans-serif;
    position: relative;
  }
  .page {
    position: absolute;
    width: 578px;
    height: 818px;
    background: var(--paper);
    overflow: hidden;
  }
  .page--front { left: 12px; top: 15px; }
  .page--back  { left: 610px; top: 55px; }

  .photo { position: absolute; left: 0; top: 0; width: 100%; }
  .photo--meeting {
    height: 330px;
    background: linear-gradient(160deg, #f4f6f9 0%, #dfe4ea 45%, #c9d0d9 100%);
  }
  .photo--laptop {
    height: 300px;
    background: linear-gradient(150deg, #2c4a86 0%, #7d93b8 40%, #d6dbe3 70%, #334d80 100%);
  }
  .swirl { position: absolute; left: 0; width: 100%; height: 120px; }
  .page--front .swirl { top: 260px; }
  .page--back .swirl { top: 230px; }

  .brand {
    position: absolute; left: 23px; top: 78px;
    color: var(--navy);
    font-weight: 700; font-size: 37px; line-height: 38px;
  }
  .brand span { display: block; padding-left: 24px; }

  .welcome {
    position: absolute; left: 20px; top: 340px; width: 256px; height: 463px;
    border-radius: 18px;
    background: linear-gradient(90deg, #2a5aa8 0%, #3f78c8 55%, #2c5fae 100%);
    color: #fff; padding: 18px 18px 0 20px;
    box-shadow: 0 4px 10px rgba(0,0,0,.25);
  }
  .welcome h1 {
    color: var(--welcome); font-size: 22px; line-height: 27px;
    text-align: center; font-weight: 700; margin-bottom: 24px;
  }
  .welcome p { font-size: 14.5px; line-height: 20.5px; margin-bottom: 20px; }
  .welcome .lead { font-size: 19px; font-weight: 700; }

  .tab {
    position: absolute; left: 310px; width: 183px; height: 36px;
    background: linear-gradient(180deg, #4f86cf 0%, #2a5aa8 100%);
    border-radius: 4px; color: #fff;
    font-family: "Oswald", "Arial Narrow", sans-serif;
    font-weight: 600; font-size: 26px; line-height: 36px; padding-left: 12px;
    box-shadow: 0 3px 6px rgba(0,0,0,.2);
  }
  .tab--develop { top: 383px; }
  .tab--implement { top: 559px; }
  .services {
    position: absolute; left: 313px; top: 434px; width: 262px;
    font-size: 13.5px; line-height: 19px; text-transform: uppercase; color: var(--ink);
  }
  .steps {
    position: absolute; left: 313px; top: 608px; list-style: none;
    font-family: "Oswald", "Arial Narrow", sans-serif; font-weight: 500;
    font-size: 22px; line-height: 33px; color: var(--grey);
  }
  .steps li::before { content: "•"; color: var(--blue-light); margin-right: 4px; }
  .address {
    position: absolute; left: 310px; top: 722px; width: 253px; height: 78px;
    background: linear-gradient(90deg, #2c5fae, #3f78c8);
    border-radius: 6px; color: #fff; font-weight: 700; font-style: normal;
    font-size: 17px; line-height: 23px; text-align: right; padding: 5px 12px 0 0;
  }

  .testimonial { position: absolute; left: 18px; width: 542px; height: 127px; }
  .testimonial--1 { top: 320px; }
  .testimonial--2 { top: 475px; }
  .testimonial--3 { top: 630px; }
  .testimonial__bar {
    position: absolute; left: 40px; top: 0; right: 0; height: 127px;
    background: var(--bar); border-radius: 14px 0 0 14px;
    box-shadow: 0 6px 8px rgba(0,0,0,.25);
  }
  .client {
    position: absolute; left: 0; top: 4px; width: 119px; height: 119px;
    border-radius: 50%; background: var(--bar);
    display: flex; align-items: center; justify-content: center;
  }
  .client__ring {
    width: 96px; height: 96px; border-radius: 50%; background: #3c9ae0;
    display: flex; align-items: center; justify-content: center;
  }
  .client__name {
    width: 78px; height: 78px; border-radius: 50%; background: #fff;
    display: flex; align-items: center; justify-content: center;
    font-weight: 700; font-size: 13px; color: var(--ink);
  }
  .quote {
    position: absolute; left: 124px; top: 5px; width: 412px;
    color: #fff; font-size: 13.3px; line-height: 20.5px;
  }
  .quote cite {
    display: block; text-align: right; padding-right: 14px;
    font-style: normal; font-weight: 700; font-size: 16px; color: #3f78c8;
  }
  .web {
    position: absolute; left: 172px; top: 771px; width: 257px; height: 30px;
    border-radius: 15px; background: linear-gradient(90deg, #2c5fae, #3f78c8);
    color: #fff; font-weight: 700; font-size: 17px; line-height: 30px; text-align: center;
  }
</style>
</head>
<body>

<section class="page page--front">
  <div class="photo photo--meeting" role="img" aria-label="Photo of a business team meeting around a glass table, seen from above"></div>
  <svg class="swirl" viewBox="0 0 578 120" preserveAspectRatio="none" aria-hidden="true">
    <defs>
      <linearGradient id="swirlFront" x1="0" x2="1">
        <stop offset="0" stop-color="#1f4fa3"/><stop offset="1" stop-color="#5aa3e6"/>
      </linearGradient>
    </defs>
    <path d="M0 45 C140 105 320 0 578 30 L578 55 C330 25 150 115 0 75 Z" fill="#9fd0f2"/>
    <path d="M0 55 C150 120 330 10 578 40 L578 70 C330 40 150 125 0 85 Z" fill="url(#swirlFront)"/>
    <path d="M0 85 C150 125 330 40 578 70 L578 120 L0 120 Z" fill="#fff"/>
  </svg>
  <div class="brand">Brightpath<span>Rewards</span></div>

  <div class="welcome">
    <h1>Welcome to Brightpath Rewards</h1>
    <p><span class="lead">The</span> Brightpath Rewards team is a creative group of professionals that will look to deliver true brand loyalty to your organisation. Experienced in a range industry sectors including: retail, FMCG, insurance, automotive, Pharmaceutical/Healthcare, telecommunications, property, and IT.</p>
    <p>We help you build customer loyalty to your brand across all channels to market</p>
  </div>

  <div class="tab tab--develop">DEVELOP</div>
  <p class="services">Brightpath Rewards specialises in strategy development, planning and implementation of customer loyalty enhancement projects.</p>
  <div class="tab tab--implement">IMPLEMENT</div>
  <ul class="steps">
    <li>DISCOVERY</li>
    <li>STRATEGY</li>
    <li>PLANNING</li>
  </ul>
  <address class="address">48 Harbour View<br>Parade<br>Eastbank VIC 3010</address>
</section>

<section class="page page--back">
  <div class="photo photo--laptop" role="img" aria-label="Photo of colleagues working at a laptop and papers on a desk"></div>
  <svg class="swirl" viewBox="0 0 578 120" preserveAspectRatio="none" aria-hidden="true">
    <defs>
      <linearGradient id="swirlBack" x1="0" x2="1">
        <stop offset="0" stop-color="#1f4fa3"/><stop offset="1" stop-color="#5aa3e6"/>
      </linearGradient>
    </defs>
    <path d="M0 40 C140 110 320 0 578 25 L578 50 C330 20 150 120 0 70 Z" fill="#9fd0f2"/>
    <path d="M0 50 C150 125 330 5 578 35 L578 65 C330 35 150 130 0 80 Z" fill="url(#swirlBack)"/>
    <path d="M0 80 C150 130 330 35 578 65 L578 120 L0 120 Z" fill="#fff"/>
  </svg>

  <article class="testimonial testimonial--1">
    <div class="testimonial__bar"></div>
    <div class="client"><div class="client__ring"><div class="client__name">Dorquin</div></div></div>
    <blockquote class="quote">“Our company is rapidly expanding and needed to bring in some high level expertise to set our direction for the future. Brightpath Rewards was chosen and wrote our strategic plan from scratch. We are excited to see the initiatives coming to life. Members of our team also love attending their quarterly Customer Loyalty events!”
      <cite>Tom Garrick, CEO &amp; Executive Director</cite></blockquote>
  </article>

  <article class="testimonial testimonial--2">
    <div class="testimonial__bar"></div>
    <div class="client"><div class="client__ring"><div class="client__name">Vessock</div></div></div>
    <blockquote class="quote" style="top:10px">“Brightpath Rewards undertook a complete assessment of our loyalty program and their recommendations have provided a clear path to uncovering how we could move forward. The customer angle was especially insightful in highlighting the gaps in our program.”
      <cite style="margin-top:8px">Kevin Barrow, Executive Vice President</cite></blockquote>
  </article>

  <article class="testimonial testimonial--3">
    <div class="testimonial__bar"></div>
    <div class="client"><div class="client__ring"><div class="client__name">Talbrook</div></div></div>
    <blockquote class="quote" style="top:24px">“The loyalty audit carried out by Brightpath Rewards has isolated some key strategic opportunities for us to focus on that will have an important part to play in the future direction of Talbrook one.”
      <cite style="margin-top:6px">Brendan Hollis, CEO – Talbrook Holdings</cite></blockquote>
  </article>

  <div class="web">www.brightpathrewards.com</div>
</section>

</body>
</html>
```